Business Card Design for Lawn Management

Lawn Management

Industry/Entity Type

Business

Contact Information for Business Card

Calloway Lawn Management
Doran Calloway
Calloway_Lawn@brindlemail.com
404-627-1845

```html
<!DOCTYPE html>
<html lang="en">
<head>
<meta charset="utf-8">
<title>Calloway Lawn Management – Business Card</title>
<link rel="stylesheet" href="https://fonts.googleapis.com/css2?family=Lato:wght@400;700;900&display=swap">
<style>
  :root {
    --page-bg: #2b2b2b;
    --card-white: #fafafa;
    --card-shade: #e6e6e6;
    --brand-green: #3a9a3c;
    --edge-green: #2f9a3a;
    --ink: #1f1f1f;
    --grass-light: #7fbf4a;
    --grass-mid: #3f8f2a;
    --grass-dark: #1f4f18;
    --on-photo: #ffffff;
  }
  * { box-sizing: border-box; margin: 0; padding: 0; }
  html, body {
    width: 1200px; height: 873px; overflow: hidden;
    background: var(--page-bg);
    font-family: "Lato", Arial, sans-serif;
  }
  .sheet {
    position: relative; width: 1200px; height: 873px;
  }
  .card {
    position: absolute; left: 320px; width: 560px; height: 320px;
    background: linear-gradient(160deg, var(--card-white) 0%, var(--card-shade) 100%);
    border-radius: 18px;
    border-bottom: 9px solid var(--edge-green);
    overflow: hidden;
  }
  .card--back { top: 90px; }
  .card--front { top: 470px; }

  /* Back side: brand name */
  .brand {
    position: absolute; inset: 0;
    display: flex; align-items: center; justify-content: center; gap: 18px;
    color: var(--brand-green); font-weight: 900;
  }
  .brand__dot {
    width: 54px; height: 54px; border-radius: 50%;
    background: var(--brand-green);
  }
  .brand__name { font-size: 34px; line-height: 1.05; text-transform: uppercase; }
  .brand__name span { display: block; }

  /* Front side */
  .person { position: absolute; left: 40px; top: 88px; }
  .person__name { color: var(--brand-green); font-weight: 900; font-size: 30px; }
  .person__role { color: var(--ink); font-size: 18px; margin-left: 70px; margin-top: 2px; }

  .contact { position: absolute; left: 40px; top: 222px; list-style: none; }
  .contact li {
    display: flex; align-items: center; gap: 12px;
    font-weight: 700; font-size: 16px; color: var(--ink); height: 32px;
  }
  .contact svg { flex: none; }

  .photo {
    position: absolute; left: 330px; top: 22px; width: 210px; height: 178px;
    border-radius: 18px;
    background: linear-gradient(180deg, var(--grass-dark) 0%, var(--grass-mid) 45%, var(--grass-light) 100%);
  }
  .photo__brand {
    position: absolute; left: 0; right: 0; bottom: 28px;
    text-align: center; color: var(--on-photo);
    font-weight: 900; font-size: 22px; line-height: 1.1; text-transform: uppercase;
  }
  .photo__brand span { display: block; }
</style>
</head>
<body>
<main class="sheet">
  <section class="card card--back" aria-label="Card back">
    <div class="brand">
      <div class="brand__dot"></div>
      <p class="brand__name"><span>Calloway</span><span>Lawn Management</span></p>
    </div>
  </section>

  <section class="card card--front" aria-label="Card front">
    <div class="person">
      <h1 class="person__name">Doran Calloway</h1>
      <p class="person__role">Owner / Founder</p>
    </div>

    <ul class="contact">
      <li>
        <svg width="14" height="20" viewBox="0 0 14 20" aria-hidden="true">
          <rect x="1.5" y="1.5" width="11" height="17" rx="2" fill="none" stroke="#3a9a3c" stroke-width="2"/>
        </svg>
        404-627-1845
      </li>
      <li>
        <svg width="20" height="14" viewBox="0 0 20 14" aria-hidden="true">
          <rect x="0" y="0" width="20" height="14" rx="1" fill="#3a9a3c"/>
          <path d="M1 1 L10 8 L19 1" fill="none" stroke="#fafafa" stroke-width="1.5"/>
        </svg>
        Calloway_Lawn@brindlemail.com
      </li>
    </ul>

    <div class="photo" role="img" aria-label="Close-up photograph of green lawn grass">
      <p class="photo__brand"><span>Calloway</span><span>Lawn Management</span></p>
    </div>
  </section>
</main>
</body>
</html>
```